Australian Software Consultancy needs new Business Card Design

Design Business Card based on existing design artefacts (attached). We are open to all designs. As its a 2 sided design and we thought it might be quite striking to have one side with a black background and te other side with a white background.

Target Market(s)

Financial Services mainly.

Industry/Entity Type

Business

Contact Information for Business Card

Name :
Position :
Email :

Requirements
Must have
• Funky design using our existing assets

```html
<!DOCTYPE html>
<html lang="en">
<head>
<meta charset="utf-8">
<title>Bright Field – Business Card</title>
<link rel="stylesheet" href="https://fonts.googleapis.com/css2?family=Lato:wght@400;700;900&display=swap">
<style>
  :root {
    --stage: #3a3a3a;
    --card-black: #1b1b1c;
    --band: #1c1c1d;
    --ink: #161616;
    --red: #e0202a;
    --light: #f2f2f2;
    --divider: #555;
  }
  * { margin: 0; padding: 0; box-sizing: border-box; }
  html, body { width: 1200px; height: 834px; overflow: hidden; }
  body {
    background: var(--stage);
    font-family: "Lato", sans-serif;
    position: relative;
  }
  .card {
    position: absolute;
    width: 560px;
    height: 320px;
    box-shadow: 0 12px 30px rgba(0,0,0,.45);
    overflow: hidden;
  }
  .card-front {
    left: 120px; top: 70px;
    background: var(--card-black);
    display: flex; align-items: center; justify-content: center;
  }
  .card-back {
    left: 520px; top: 444px;
    background: linear-gradient(135deg, #f7f7f7, #e4e4e4);
  }
  .wordmark {
    font-weight: 900;
    text-transform: uppercase;
    letter-spacing: 1px;
    line-height: 1;
    white-space: nowrap;
  }
  .card-front .wordmark { color: var(--light); font-size: 46px; }
  .brand-block {
    position: absolute; left: 0; right: 0; top: 0; height: 190px;
    display: flex; align-items: center; justify-content: center;
  }
  .card-back .wordmark { color: var(--ink); font-size: 34px; }
  .contact-band {
    position: absolute; left: 0; right: 0; top: 190px; height: 72px;
    background: var(--band);
    display: flex; align-items: center;
  }
  .person {
    width: 270px; text-align: right; padding-right: 18px;
    border-right: 1px solid var(--divider);
  }
  .person-name { color: var(--light); font-weight: 700; font-size: 17px; }
  .person-role { color: var(--red); font-size: 14px; margin-top: 2px; }
  .details { padding-left: 18px; display: flex; flex-direction: column; gap: 6px; }
  .detail { display: flex; align-items: center; gap: 10px; color: var(--light); font-size: 13px; }
  .detail svg { width: 13px; height: 13px; flex: none; }
</style>
</head>
<body>
  <section class="card card-front">
    <span class="wordmark">Bright Field</span>
  </section>

  <section class="card card-back">
    <div class="brand-block">
      <span class="wordmark">Bright Field</span>
    </div>
    <div class="contact-band">
      <div class="person">
        <div class="person-name">Alex Morgan</div>
        <div class="person-role">President</div>
      </div>
      <div class="details">
        <div class="detail">
          <svg viewBox="0 0 16 16" aria-hidden="true"><path d="M3 1.5l3 .5 1 3-1.7 1.3a9 9 0 0 0 4.4 4.4L11 9l3 1 .5 3-2 1.5C7 14 2 9 1.5 3.5z" fill="none" stroke="#e0202a" stroke-width="1.4"/></svg>
          <span>9100 450 450</span>
        </div>
        <div class="detail">
          <svg viewBox="0 0 16 16" aria-hidden="true"><rect x="1.5" y="3.5" width="13" height="9" fill="none" stroke="#e0202a" stroke-width="1.4"/><path d="M1.5 3.5 8 9l6.5-5.5" fill="none" stroke="#e0202a" stroke-width="1.4"/></svg>
          <span>alex@email.com</span>
        </div>
      </div>
    </div>
  </section>
</body>
</html>
```